Personal Training Boot Camp Poster

We need a poster design for a 2 upcoming boot camps which are called
Iron Forge, and Peak Blitz. We would like to see designs that incorporate our logo. We want the poster to be very appealing to clients.

Dates: February 2 - March 19th

Iron Forge : Monday's and Wednesday's 8pm-9pm
Peak Blitz : Tuesday's and Thursdays 8pm-9pm

Training

```html
<!DOCTYPE html>
<html lang="en">
<head>
<meta charset="utf-8">
<title>Personal Training Boot Camp Poster</title>
<link rel="stylesheet" href="https://fonts.googleapis.com/css2?family=Oswald:wght@400;600;700&family=Roboto+Condensed:wght@400;500&display=swap">
<style>
  :root {
    --page-bg: #e9e8e6;
    --poster-black: #050505;
    --brand-orange: #ef6a22;
    --accent-red: #e2452b;
    --headline-grey: #b9b9b9;
    --text-white: #f2f2f2;
    --tagline-grey: #9a9a9a;
    --photo-dark: #0d1a22;
    --photo-teal: #1d6f78;
    --photo-light: #c9d6dc;
  }
  * { box-sizing: border-box; margin: 0; padding: 0; }
  html, body {
    width: 1200px;
    height: 1148px;
    overflow: hidden;
    background: var(--page-bg);
  }
  .poster {
    position: absolute;
    left: 240px;
    top: 64px;
    width: 720px;
    height: 1020px;
    background: var(--poster-black);
    display: flex;
    flex-direction: column;
  }
  .poster-header {
    height: 200px;
    flex: none;
    display: flex;
    flex-direction: column;
    align-items: center;
    justify-content: center;
    gap: 10px;
  }
  .brand-row {
    display: flex;
    align-items: center;
    gap: 14px;
  }
  .brand-square {
    width: 34px;
    height: 34px;
    background: var(--brand-orange);
  }
  .brand-name {
    font-family: "Oswald", sans-serif;
    font-weight: 400;
    font-size: 44px;
    letter-spacing: 4px;
    color: var(--brand-orange);
    text-transform: uppercase;
  }
  .brand-tagline {
    font-family: "Roboto Condensed", sans-serif;
    font-size: 13px;
    letter-spacing: 3px;
    color: var(--tagline-grey);
    text-transform: uppercase;
  }
  .hero-photo {
    height: 540px;
    flex: none;
    background:
      radial-gradient(ellipse 45% 35% at 22% 55%, rgba(201,214,220,0.75), transparent 70%),
      radial-gradient(ellipse 40% 40% at 80% 50%, rgba(29,111,120,0.9), transparent 75%),
      linear-gradient(180deg, #1a2a33 0%, var(--photo-dark) 30%, #22414a 60%, var(--photo-dark) 100%);
  }
  .poster-footer {
    flex: 1;
    padding: 26px 48px 40px;
    display: flex;
    flex-direction: column;
  }
  .headline {
    font-family: "Oswald", sans-serif;
    font-weight: 700;
    font-size: 42px;
    line-height: 1;
    white-space: nowrap;
    color: var(--headline-grey);
    text-align: center;
    text-transform: uppercase;
  }
  .date-rule {
    display: flex;
    align-items: center;
    gap: 10px;
    margin-top: 10px;
  }
  .date-rule .line {
    flex: 1;
    height: 3px;
    background: var(--accent-red);
  }
  .date-rule .dates {
    font-family: "Oswald", sans-serif;
    font-weight: 600;
    font-size: 19px;
    color: var(--accent-red);
    text-transform: uppercase;
  }
  .sessions {
    display: flex;
    justify-content: space-between;
    margin-top: 26px;
  }
  .session { display: flex; flex-direction: column; gap: 6px; }
  .session--right { text-align: right; margin-top: -12px; }
  .session-name {
    font-family: "Roboto Condensed", sans-serif;
    font-weight: 500;
    font-size: 21px;
    color: var(--text-white);
    text-transform: uppercase;
    margin-bottom: 6px;
  }
  .session-time {
    font-family: "Roboto Condensed", sans-serif;
    font-size: 21px;
    line-height: 1.2;
    color: var(--accent-red);
    text-transform: uppercase;
  }
</style>
</head>
<body>
  <main class="poster">
    <header class="poster-header">
      <div class="brand-row">
        <span class="brand-square"></span>
        <span class="brand-name">Summit Vantage</span>
      </div>
      <p class="brand-tagline">Move Better · Get Faster · Be Stronger</p>
    </header>

    <div class="hero-photo" role="img" aria-label="Athlete in a white sports top sprinting against a blurred teal light background"></div>

    <section class="poster-footer">
      <h1 class="headline">Personal Training Boot Camp</h1>
      <div class="date-rule">
        <span class="line"></span>
        <span class="dates">February 2 - March 19th</span>
        <span class="line"></span>
      </div>
      <div class="sessions">
        <div class="session session--left">
          <h2 class="session-name">Iron Forge</h2>
          <p class="session-time">Monday's and Wednesday's<br>8pm-9pm</p>
        </div>
        <div class="session session--right">
          <h2 class="session-name">Peak Blitz</h2>
          <p class="session-time">Tuesday's and Thursdays<br>8pm-9pm</p>
        </div>
      </div>
    </section>
  </main>
</body>
</html>
```